Electrical Contracting Business Website

Require website done for my contracting business.
Partly done one but really dont have time.

You can view the current one at http://corvane.net.au

You can use any info/styles/photos from the current website

I like the orange color of the logo so id like things to be with that
Unfortunatly being a new business (Sept 2015) I havent got alot of photos . but if you require any for any of the specifics listed in the doc file ill have a look to see what I have.

I am targeting mainly commercial / industrial clients. Which also includes government and mining.

Target Market(s)

People requiring electricians

Industry/Entity Type

Electrician

Coding

Number of Pages Required

Colors
f37122

Requirements
Must have
• logo with EC Number
• Keep it simple and not to complicated
• Comply with the current html / style sheet standards.
• Desktop/Mobile Version compatability
Nice to have
• additional photos.
• The domestic lifts we install are by vostrel I dont have any photos of them unfortunately.
Should not have
• change colour of logo

```html
<!DOCTYPE html>
<html lang="en">
<head>
<meta charset="utf-8">
<title>Corvane Engineering – Electrical Services</title>
<link href="https://fonts.googleapis.com/css2?family=Oswald:wght@300;400;500&family=Arimo:wght@400;700&display=swap" rel="stylesheet">
<style>
:root{
  --orange:#f37122;
  --dark:#2b2b2b;
  --white:#ffffff;
  --grey-welcome:#d9d9d9;
  --grey-light:#ebebeb;
  --grey-form:#d6d6d6;
  --social:#c9dbe8;
  --text:#1e1e1e;
  --muted:#555555;
}
*{box-sizing:border-box;margin:0;padding:0}
html,body{width:1200px;height:2507px;overflow:hidden}
body{position:relative;background:var(--white);font-family:"Arimo",Arial,sans-serif;color:var(--text)}
.abs{position:absolute}
.display{font-family:"Oswald","Arial Narrow",sans-serif}

/* header */
.topbar{left:0;top:0;width:1200px;height:92px;background:var(--dark)}
.brand{left:92px;top:14px;display:flex;align-items:center;gap:12px}
.brand-dot{width:52px;height:52px;border-radius:50%;background:var(--orange)}
.brand-name{font-family:"Oswald",sans-serif;font-weight:500;font-size:42px;color:var(--orange);letter-spacing:2px;line-height:1}
.top-phone{left:628px;top:38px;font-weight:700;font-size:18px;color:var(--white);letter-spacing:1px}
.callback{left:900px;top:32px;width:169px;height:42px;background:var(--orange);border-radius:3px;display:flex;align-items:center;gap:10px;padding-left:12px;color:var(--dark);font-weight:700;font-size:13px;letter-spacing:.5px}
.mainnav{left:0;top:92px;width:1200px;height:40px;background:var(--orange);display:flex;justify-content:center;align-items:center;gap:26px;padding-right:40px}
.mainnav a{color:var(--white);text-decoration:none;font-weight:700;font-size:17px;letter-spacing:1px;display:flex;align-items:center;gap:6px}

/* hero */
.hero{left:0;top:132px;width:1200px;height:505px;background:linear-gradient(100deg,#c9a48e 0%,#d8d4cf 30%,#ece9e4 55%,#4a5a66 75%,#2e9ad0 100%)}
.hero-title{left:117px;top:196px;font-size:56px;line-height:58px;color:var(--white);font-weight:300}
.hero-sub{left:117px;top:346px;font-size:34px;color:var(--white);font-weight:400}
.hero-list{left:117px;top:404px;list-style:none;font-size:14px;line-height:16px;color:var(--white)}
.hero-arrow{top:336px}
.social{left:1140px;width:60px;height:60px;background:var(--social);opacity:.85;z-index:5}

/* features */
.features{left:0;top:637px;width:1200px;height:103px;background:var(--white)}
.feature{top:24px;display:flex;gap:14px}
.feature h3{font-family:"Oswald",sans-serif;font-weight:400;font-size:22px;line-height:26px;color:var(--text)}
.feature p{font-size:10px;color:var(--muted)}

/* welcome */
.welcome{left:0;top:740px;width:1200px;height:335px;background:var(--grey-welcome)}
.van{left:175px;top:62px;width:410px;height:176px;border-radius:14px 60px 10px 10px;background:linear-gradient(180deg,#fafafa,#d2d2d2)}
.welcome h2{left:613px;top:54px;font-size:27px;letter-spacing:2px;font-weight:700}
.welcome p{left:613px;top:114px;width:420px;font-size:16.5px;line-height:24px;font-weight:700;letter-spacing:1.4px}
.welcome p span{color:var(--orange);font-style:italic}
.btn{background:var(--orange);color:var(--white);font-family:"Oswald",sans-serif;display:flex;align-items:center;justify-content:center;gap:6px;font-size:17px}
.welcome .btn{left:613px;top:239px;width:129px;height:39px}

/* projects */
.projects{left:0;top:1075px;width:1200px;height:835px;background:var(--grey-light)}
.section-title{font-weight:700;font-size:28px;letter-spacing:2px}
.projects .section-title{left:132px;top:50px}
.tile{width:224px;height:171px;background:var(--orange);padding:10px}
.tile div{width:100%;height:100%}
.load-more{left:535px;top:506px;width:127px;height:38px;font-family:"Arimo",sans-serif;font-weight:700;font-size:13px}
.projects .center-title{left:0;top:594px;width:1200px;text-align:center}
.service{top:663px;width:200px;text-align:center}
.service .ring{width:86px;height:86px;border-radius:50%;background:var(--white);margin:0 auto;display:flex;align-items:center;justify-content:center}
.service .ring span{width:70px;height:70px;border-radius:50%;background:var(--orange);display:flex;align-items:center;justify-content:center}
.service p{margin-top:16px;font-weight:700;font-size:15px;letter-spacing:1px;line-height:19px}
.svc-arrow{top:682px}

/* appointment */
.booking{left:0;top:1910px;width:1200px;height:338px;background:var(--grey-form)}
.booking .section-title{top:30px}
.label{font-size:14px;color:var(--text)}
.field{height:28px;background:var(--white)}
.captcha{left:130px;top:206px;width:107px;height:36px;background:linear-gradient(90deg,#e9e9e9,#f7f7f7,#e4e4e4)}
.change{color:var(--orange)}
.submit{left:132px;top:271px;width:122px;height:43px;font-size:19px}
.testimonial{left:767px;top:82px;width:293px;height:236px;background:var(--white);padding:12px 16px 12px 52px;font-size:11.5px;line-height:15px;color:#555}
.testimonial .bar{position:absolute;right:10px;top:8px;width:4px;height:60px;background:var(--orange)}
.testimonial .who{color:var(--orange);font-size:10px;margin-bottom:10px}
.testimonial .who b{color:#777;font-weight:400}

/* footer */
.footer{left:0;top:2248px;width:1200px;height:214px;background:var(--dark);color:var(--white)}
.foot-brand{left:134px;top:38px;display:flex;align-items:center;gap:12px}
.foot-brand .brand-dot{width:60px;height:60px}
.foot-brand .brand-name{font-size:50px}
.reg{left:205px;top:128px;font-size:9px;line-height:12px;color:var(--orange);width:200px}
.foot-col h4{font-weight:700;font-size:20px;letter-spacing:1.5px}
.foot-col ul{list-style:none;margin-top:24px}
.foot-col li{font-weight:700;font-size:14.5px;line-height:22.5px;letter-spacing:.8px}
.contact-line{display:flex;align-items:center;gap:12px;font-weight:700;font-size:15px;letter-spacing:.8px;height:29px}
.copyright{left:0;top:2462px;width:1200px;height:45px;background:var(--orange);color:var(--white);font-weight:700;font-size:15px;letter-spacing:1px;display:flex;align-items:center;justify-content:center}
</style>
</head>
<body>

<header>
  <div class="abs topbar">
    <div class="abs brand"><span class="brand-dot"></span><span class="brand-name">CORVANE</span></div>
    <div class="abs top-phone">24/7 CALL +61 0400 317 862</div>
    <div class="abs callback">
      <svg width="14" height="24" viewBox="0 0 14 24"><rect x="1" y="1" width="12" height="22" rx="2" fill="none" stroke="#2b2b2b" stroke-width="2"/><circle cx="7" cy="19" r="1.5" fill="#2b2b2b"/></svg>
      REQUEST A CALL
    </div>
  </div>
  <nav class="abs mainnav">
    <a href="#"><svg width="16" height="16" viewBox="0 0 16 16"><path d="M8 1 1 8h2v7h4v-4h2v4h4V8h2z" fill="#fff"/></svg>HOME</a>
    <a href="#">ABOUT US</a>
    <a href="#">RESIDENTIAL</a>
    <a href="#">COMMERCIAL</a>
    <a href="#">INDUSTRIAL</a>
    <a href="#">CONTACT US</a>
  </nav>
</header>

<section class="abs hero" role="img" aria-label="Photo of a hand testing a switchboard terminal with multimeter probes"></section>
<h1 class="abs display hero-title">ELECTRICAL<br>SERVICES</h1>
<h2 class="abs display hero-sub">DIAGNOSIS AND REPAIR</h2>
<ul class="abs hero-list">
  <li>- Electrical Safety Inspections</li>
  <li>- Service Upgrades</li>
  <li>- Complete Electrical Contractor</li>
  <li>- Electrical Troubleshooting</li>
</ul>
<svg class="abs hero-arrow" style="left:22px" width="38" height="52" viewBox="0 0 38 52"><path d="M32 4 8 26l24 22" fill="none" stroke="#f37122" stroke-width="9"/></svg>
<svg class="abs hero-arrow" style="left:1140px" width="38" height="52" viewBox="0 0 38 52"><path d="M6 4l24 22L6 48" fill="none" stroke="#f37122" stroke-width="9"/></svg>

<section class="abs features">
  <div class="abs feature" style="left:132px">
    <svg width="48" height="48" viewBox="0 0 48 48"><circle cx="24" cy="16" r="9" fill="#f37122"/><path d="M12 16h24" stroke="#f37122" stroke-width="4"/><path d="M8 46c0-12 7-18 16-18s16 6 16 18z" fill="#f37122"/></svg>
    <div><h3>DIAGNOSIS AND REPAIR</h3><p>We're available 24/7</p></div>
  </div>
  <div class="abs feature" style="left:474px">
    <svg width="48" height="48" viewBox="0 0 48 48"><path d="M8 8l32 32M40 8 8 40" stroke="#f37122" stroke-width="7" stroke-linecap="round"/></svg>
    <div><h3>INSTAL AND UPGRADES</h3><p>Quality guarantee</p></div>
  </div>
  <div class="abs feature" style="left:818px">
    <svg width="48" height="48" viewBox="0 0 48 48"><path d="M18 6v10M30 6v10" stroke="#f37122" stroke-width="4"/><path d="M12 16h24v8a12 12 0 0 1-24 0z" fill="#f37122"/><path d="M24 36v6H14" stroke="#f37122" stroke-width="4" fill="none"/></svg>
    <div><h3>ELECTRICAL SYSTEM<br>MAINTENANCE</h3></div>
  </div>
</section>

<section class="abs welcome">
  <div class="abs van" role="img" aria-label="Photo of the white company service van"></div>
  <h2 class="abs">WELCOME</h2>
  <p class="abs">DELIVERING UNBEATABLE ELECTRICAL<br>SERVICES.<span>CONTACT US</span> NOW TO<br>FIND OUT HOW WE CAN HELP YOU<br>WITH YOUR NEXT ELECTRICAL SOLUTION.</p>
  <div class="abs btn">
    <svg width="10" height="14" viewBox="0 0 10 14"><path d="M6 0 0 8h4l-1 6 7-8H6z" fill="#fff"/></svg>READ MORE
  </div>
</section>

<div class="abs social" style="top:577px" aria-label="Social profile link"></div>
<div class="abs social" style="top:650px" aria-label="Social profile link"></div>
<div class="abs social" style="top:722px" aria-label="Video channel link"></div>

<section class="abs projects">
  <h2 class="abs section-title">RECENT PROJECTS</h2>
  <div class="abs tile" style="left:132px;top:126px"><div role="img" aria-label="Project photo: circuit breakers in a board" style="background:linear-gradient(180deg,#3a3a3a,#d8d8d8 45%,#4a4a4a)"></div></div>
  <div class="abs tile" style="left:364px;top:126px"><div role="img" aria-label="Project photo: motors on a frame" style="background:linear-gradient(160deg,#dcdcdc,#3b3b3b 60%,#8a8a8a)"></div></div>
  <div class="abs tile" style="left:596px;top:126px"><div role="img" aria-label="Project photo: controller display with buttons" style="background:radial-gradient(circle at 55% 35%,#b8d960 0,#b8d960 18%,#1f1f1f 40%)"></div></div>
  <div class="abs tile" style="left:828px;top:126px"><div role="img" aria-label="Project photo: wiring inside an enclosure" style="background:linear-gradient(135deg,#c8793a,#e0a050 50%,#5b3b2a)"></div></div>
  <div class="abs tile" style="left:132px;top:305px"><div role="img" aria-label="Project photo: isolator and meters on a wall" style="background:linear-gradient(180deg,#e8e8e6,#b8bab6 70%,#9c9c9c)"></div></div>
  <div class="abs tile" style="left:364px;top:305px"><div role="img" aria-label="Project photo: red emergency stop buttons" style="background:linear-gradient(135deg,#2a2a2a,#c33 45%,#d9b24a 70%,#e6e6e6)"></div></div>
  <div class="abs tile" style="left:596px;top:305px"><div role="img" aria-label="Project photo: switchgear with blue cabling" style="background:linear-gradient(180deg,#e4e4e4,#2c4e8c 75%,#1e2a4a)"></div></div>
  <div class="abs tile" style="left:828px;top:305px"><div role="img" aria-label="Project video: switchboard inspection" style="background:linear-gradient(135deg,#f2f2f2,#cfcfcf 55%,#3a3a3a)"></div></div>
  <div class="abs btn load-more">
    <svg width="10" height="14" viewBox="0 0 10 14"><path d="M6 0 0 8h4l-1 6 7-8H6z" fill="#fff"/></svg>LOAD MORE
  </div>

  <h2 class="abs section-title center-title">OUR GENERAL SERVICES</h2>
  <svg class="abs svc-arrow" style="left:132px" width="36" height="56" viewBox="0 0 36 56"><path d="M30 4 8 28l22 24" fill="none" stroke="#f37122" stroke-width="10"/></svg>
  <svg class="abs svc-arrow" style="left:1018px" width="36" height="56" viewBox="0 0 36 56"><path d="M6 4l22 24L6 52" fill="none" stroke="#f37122" stroke-width="10"/></svg>

  <div class="abs service" style="left:167px">
    <div class="ring"><span><svg width="40" height="40" viewBox="0 0 40 40"><circle cx="20" cy="20" r="15" fill="none" stroke="#fff" stroke-width="3"/><path d="M12 28 28 12M16 14l10 10" stroke="#fff" stroke-width="4"/></svg></span></div>
    <p>ELECTRICAL<br>INSTALLATIONS</p>
  </div>
  <div class="abs service" style="left:395px">
    <div class="ring"><svg width="52" height="52" viewBox="0 0 52 52"><path d="M6 36 22 20l10 10-16 16z" fill="#f37122"/><path d="M22 20l6-6M32 30l6-6" stroke="#f37122" stroke-width="4"/><path d="M36 16c6-6 10-2 12-8" fill="none" stroke="#f37122" stroke-width="3"/></svg></div>
    <p>GENERATOR<br>HOOKUP</p>
  </div>
  <div class="abs service" style="left:615px">
    <div class="ring"><svg width="50" height="50" viewBox="0 0 50 50"><path d="M8 6h34v20c0 10-8 16-17 20C16 42 8 36 8 26z" fill="#f37122"/><path d="M28 12 18 27h7l-3 11 10-15h-7z" fill="#fff"/></svg></div>
    <p>SURGE<br>PROTECTION</p>
  </div>
  <div class="abs service" style="left:817px">
    <div class="ring"><svg width="48" height="48" viewBox="0 0 48 48"><rect x="6" y="18" width="14" height="26" fill="none" stroke="#f37122" stroke-width="3"/><rect x="20" y="6" width="22" height="38" fill="none" stroke="#f37122" stroke-width="3"/><path d="M26 13h4M34 13h4M26 21h4M34 21h4M26 29h4M34 29h4M10 26h6M10 34h6" stroke="#f37122" stroke-width="3"/></svg></div>
    <p>BUILDING<br>MAINTENANCE</p>
  </div>
</section>

<section class="abs booking">
  <h2 class="abs section-title" style="left:132px">SCHEDULE APPOINTMENT</h2>
  <span class="abs label" style="left:132px;top:89px">First name:</span>
  <div class="abs field" style="left:212px;top:83px;width:211px"></div>
  <span class="abs label" style="left:450px;top:89px">Last Name:</span>
  <div class="abs field" style="left:530px;top:83px;width:210px"></div>
  <span class="abs label" style="left:132px;top:126px">Address:</span>
  <div class="abs field" style="left:212px;top:120px;width:211px"></div>
  <span class="abs label" style="left:450px;top:126px">Apt./Suite:</span>
  <div class="abs field" style="left:530px;top:120px;width:210px"></div>
  <span class="abs label" style="left:132px;top:163px">Phone:</span>
  <div class="abs field" style="left:212px;top:158px;width:63px"></div>
  <div class="abs field" style="left:287px;top:158px;width:63px"></div>
  <div class="abs field" style="left:361px;top:158px;width:62px"></div>
  <span class="abs label" style="left:450px;top:160px">Email:</span>
  <div class="abs field" style="left:530px;top:158px;width:210px"></div>
  <div class="abs captcha" role="img" aria-label="Verification image"></div>
  <span class="abs label" style="left:291px;top:212px">Verification</span>
  <div class="abs field" style="left:371px;top:206px;width:105px"></div>
  <span class="abs label" style="left:496px;top:213px;font-size:12px">Can't read image? <span class="change">Change it.</span></span>
  <div class="abs btn submit">
    <svg width="18" height="18" viewBox="0 0 18 18"><path d="M5 4a7 7 0 1 0 8 0" fill="none" stroke="#fff" stroke-width="2.2"/><path d="M9 1v8" stroke="#fff" stroke-width="2.2"/></svg>SUBMIT
  </div>

  <h2 class="abs section-title" style="left:762px">TESTIMONIALS</h2>
  <div class="abs testimonial">
    <svg class="abs" style="left:12px;top:12px" width="30" height="22" viewBox="0 0 30 22"><path d="M2 22V10C2 4 6 1 12 0v4c-3 1-5 3-5 6h5v12zM17 22V10c0-6 4-9 10-10v4c-3 1-5 3-5 6h5v12z" fill="#e4e4e4"/></svg>
    <span class="bar"></span>
    <p class="who">Cras condimentum, <b>homeowner</b></p>
    <p>Duis sollicitudin, dui ac commodo iaculis, mi mcorper nec, eleifend at, fermentum ut, turpis. Mauris et ligula quis erat dignissim.</p>
    <p style="margin-top:10px">Duis sollicitudin, dui ac commodo iaculis, mi risus sagittis odio, vel ultrices enim sem ut pede. Aenean quam. Nulla neque purus, ullamcorper nec, eleifend at, fermentum ut, turpis. Mauris et ligula quis erat dignissim imperdiet. Integer ligula magna, dictum et, pulvinar non, ultricies ac, nibh.</p>
  </div>
</section>

<footer>
  <div class="abs footer">
    <div class="abs foot-brand"><span class="brand-dot"></span><span class="brand-name">CORVANE</span></div>
    <div class="abs reg">ACN: 600 000 114<br>ABN: 00 000 000 228 &nbsp;&nbsp; EC LIC: 00417</div>

    <div class="abs foot-col" style="left:424px;top:32px">
      <h4>INFORMATION</h4>
      <ul><li>About Us</li><li>Privacy Notice</li><li>Condition of Use</li></ul>
    </div>
    <div class="abs foot-col" style="left:610px;top:32px">
      <h4>CUSTOMER SERVICE</h4>
      <ul><li>Online Support</li><li>Help &amp; FAQ's</li><li>Call Center</li></ul>
    </div>
    <div class="abs foot-col" style="left:866px;top:28px">
      <h4>CONTACT US</h4>
      <p style="margin:20px 0 4px 26px;font-weight:700;font-size:15px;line-height:20px;letter-spacing:.8px">Ridgeway, Western<br>Australia, 6090.</p>
      <div class="contact-line">
        <svg width="16" height="16" viewBox="0 0 16 16"><path d="M3 1l3 3-2 2c1 2 3 4 5 5l2-2 3 3-2 3C7 14 2 9 1 3z" fill="#f37122"/></svg>+61 0400 317 862</div>
      <div class="contact-line">
        <svg width="16" height="16" viewBox="0 0 16 16"><path d="M1 5c4-4 10-4 14 0l-2 2-2-1V4H5v2L3 7z" fill="#f37122"/><rect x="3" y="9" width="10" height="6" rx="1" fill="#f37122"/></svg>+61 (08) 6000 4821</div>
      <div class="contact-line">
        <svg width="16" height="12" viewBox="0 0 16 12"><rect x="1" y="1" width="14" height="10" fill="none" stroke="#f37122" stroke-width="1.6"/><path d="M1 1l7 6 7-6" fill="none" stroke="#f37122" stroke-width="1.6"/></svg>info@corvane.net.au</div>
    </div>
    <svg class="abs" style="left:1148px;top:46px" width="34" height="56" viewBox="0 0 34 56"><path d="M17 3a14 14 0 0 0-8 25c2 2 3 5 3 8h10c0-3 1-6 3-8A14 14 0 0 0 17 3z" fill="none" stroke="#f37122" stroke-width="3"/><path d="M12 42h10M12 47h10M14 52h6" stroke="#f37122" stroke-width="3"/><path d="M13 20l4 6 4-6" fill="none" stroke="#f37122" stroke-width="2"/></svg>
  </div>
  <div class="abs copyright">Copyright © 2016 CORVANE ENGINEERING PTY LTD</div>
</footer>

</body>
</html>
```